New modern business card design

To design a brand new business card that's clean & modern in terms of layout.
I have attached our company logo and also basic information regarding what is needed on the card that also needs to be editable.

Target Market(s)

motor trade

Contact Information for Business Card

logo, name, title, tel, mob, email, address, www, all information is in the word.doc file

Requirements
Must have
• white background
Nice to have
• Nice clean font

```html
<!DOCTYPE html>
<html lang="en">
<head>
<meta charset="utf-8">
<title>Northgate Fixings Ltd – Business Card</title>
<link rel="stylesheet" href="https://fonts.googleapis.com/css2?family=Arimo:wght@400;700&family=Open+Sans:wght@600;700&display=swap">
<style>
  :root {
    --page-bg: #2b2b2b;
    --card-bg: #ffffff;
    --brand-blue: #1f6cb0;
    --ink: #1d1d1d;
    --band-grey: #a9abae;
    --band-grey-light: #e4e5e7;
    --band-text: #f4f4f4;
  }
  * { box-sizing: border-box; margin: 0; padding: 0; }
  html, body {
    width: 1200px; height: 997px; overflow: hidden;
    background: var(--page-bg);
  }
  .card {
    position: absolute; left: 180px; top: 258px;
    width: 840px; height: 480px;
    background: var(--card-bg);
    font-family: "Arimo", Arial, sans-serif;
    color: var(--ink);
    overflow: hidden;
    box-shadow: 0 18px 40px rgba(0,0,0,.45);
  }
  .brand {
    position: absolute; left: 52px; top: 122px;
    display: flex; align-items: center; gap: 12px;
  }
  .brand__mark { width: 22px; height: 22px; background: var(--brand-blue); flex: none; }
  .brand__name {
    font-weight: 700; font-size: 26px; letter-spacing: .5px;
    color: var(--brand-blue); line-height: 1; white-space: nowrap;
  }
  .brand__suffix {
    position: absolute; left: 200px; top: 155px;
    font-size: 13px; letter-spacing: 8px; color: var(--band-grey);
    line-height: 1;
  }
  .rule { position: absolute; height: 2px; background: var(--brand-blue); }
  .rule--brand { left: 40px; top: 175px; width: 390px; }
  .rule--mid { left: 445px; top: 143px; width: 365px; }
  .rule--name { left: 500px; top: 96px; width: 310px; }

  .person { position: absolute; right: 34px; top: 52px; text-align: right; }
  .person__name { font-weight: 700; font-size: 19px; color: var(--brand-blue); letter-spacing: .5px; }
  .person__title { font-size: 15px; margin-top: 2px; }

  .contacts {
    position: absolute; right: 34px; top: 162px;
    list-style: none; text-align: right; font-size: 16px; line-height: 1;
  }
  .contacts li { display: flex; justify-content: flex-end; align-items: center; gap: 12px; height: 26px; }
  .contacts .icon { width: 18px; height: 18px; }
  .contacts .email { margin-top: 16px; }

  .address {
    position: absolute; left: 52px; top: 310px;
    font-size: 18px; line-height: 1.3; color: var(--brand-blue);
    font-style: normal;
  }

  .band-light {
    position: absolute; left: 0; bottom: 62px; width: 470px; height: 40px;
    background: var(--band-grey-light);
  }
  .band-tagline {
    position: absolute; left: 0; bottom: 0; width: 470px; height: 62px;
    background: var(--band-grey);
    color: var(--band-text); font-size: 22px;
    display: flex; align-items: center; padding-left: 52px;
  }
  .band-web {
    position: absolute; right: 0; bottom: 0; width: 370px; height: 102px;
    background: var(--brand-blue);
    color: #ffffff; font-family: "Open Sans", Arial, sans-serif;
    font-weight: 700; font-size: 20px; letter-spacing: .5px;
    display: flex; align-items: flex-start; justify-content: flex-end;
    padding: 16px 30px 0 0;
  }
</style>
</head>
<body>
  <article class="card">
    <div class="brand">
      <span class="brand__mark"></span>
      <span class="brand__name">NORTHGATE FIXINGS</span>
    </div>
    <span class="brand__suffix">LTD</span>
    <div class="rule rule--brand"></div>
    <div class="rule rule--mid"></div>

    <div class="person">
      <p class="person__name">DANIEL HARPER</p>
      <p class="person__title">General Manager</p>
    </div>
    <div class="rule rule--name"></div>

    <ul class="contacts">
      <li>0161 555 0192
        <svg class="icon" viewBox="0 0 20 20" aria-hidden="true"><circle cx="10" cy="10" r="10" fill="#1f6cb0"/><path d="M6 8c0-1 1-2 4-2s4 1 4 2v1h-2V8H8v1H6z M7 10h6l1 4H6z" fill="#fff"/></svg>
      </li>
      <li>07700 900 418
        <svg class="icon" viewBox="0 0 20 20" aria-hidden="true"><circle cx="10" cy="10" r="10" fill="#1f6cb0"/><rect x="7" y="4.5" width="6" height="11" rx="1" fill="#fff"/><rect x="8" y="6" width="4" height="7" fill="#1f6cb0"/></svg>
      </li>
      <li>www.northgate-fixings.co.uk
        <svg class="icon" viewBox="0 0 20 20" aria-hidden="true"><circle cx="10" cy="10" r="10" fill="#1f6cb0"/><rect x="5" y="6.5" width="10" height="7" fill="#fff"/><path d="M5 6.5l5 4 5-4" fill="none" stroke="#1f6cb0" stroke-width="1"/></svg>
      </li>
      <li class="email">dharper@northgate-fixings.co.uk</li>
    </ul>

    <address class="address">
      Carver Street Halewood<br>Leeds LS9 4QT
    </address>

    <div class="band-light"></div>
    <div class="band-tagline">Call Today For a Free Quote</div>
    <div class="band-web">www.northgate-fixings.co.uk</div>
  </article>
</body>
</html>
```